Solar panel installation company needs a flyer.

Need a double sided flyer (not sure what size at this stage) to attract new customers and engage them with our company. We supply and install solar panels for residential homes and want residents to see the sense in installing solar.
Ideally we need on the front page:
A photo of us installing solar panels so the customer can see the face of our business and who they are dealing with.
A question: "What will your electricity bill look like in 5 years time?"
An answer to the above question: "Install solar power today and start saving!" (with a picture of solar panels on roof and money underneath - see attached)
A section that says: "3 reasons to install solar..."
1 - "The sun provides ample amounts of free, clean energy every day."
2 - "The government provides generous incentives saving you thousands of $$."
3 - "Advanced technology allows you to store your energy and use it a night."
A call to action such as: "Call us now for a free quote." (Phone 0482 917 605).
Back page we need:
A simple table showing a price guide with original cost crossed out and discounted cost highlighted. And a section with more information under the table.
A section about our company with a picture of us.
A customer testimonial.
A footer section with more information such as business number, license numbers, website and terms of the price guide.
We want you to come up with creative, eye catching and easy to read ways to display the above information with enough white space so it doesn't seem too busy. We are open to other suggestions, colour scheme and amount of information that should be placed on the flyer.
We also need to display our website on both sides (www.tarnbrookservices.com.au)
Please find attached photos, logos and content for you to use in the best way possible.
If you feel images are not of quality we can arrange professional images to be taken and uploaded.
Home owners aged 30+
It Company

```html
<!DOCTYPE html>
<html lang="en">
<head>
<meta charset="utf-8">
<title>Tarnbrook Solar &amp; Electrical – Flyer</title>
<link rel="stylesheet" href="https://fonts.googleapis.com/css2?family=Oswald:wght@500;700&family=Open+Sans:wght@700;800&display=swap">
<style>
  :root {
    --orange: #f7941d;
    --orange-deep: #ef7d10;
    --ink: #1a1a1a;
    --paper: #ffffff;
    --sky: #7fb2d9;
    --panel: #2a4f86;
  }
  * { box-sizing: border-box; margin: 0; padding: 0; }
  html, body { width: 849px; height: 1200px; overflow: hidden; background: var(--paper); }
  .flyer {
    position: relative;
    width: 849px;
    height: 1200px;
    background: var(--paper);
    font-family: "Oswald", sans-serif;
    overflow: hidden;
  }
  .top-stripe { position: absolute; left: 0; top: 0; width: 849px; height: 170px; }
  .brand {
    position: absolute;
    left: 22px;
    top: 14px;
    display: flex;
    align-items: center;
    gap: 14px;
    z-index: 2;
  }
  .brand-dot {
    width: 128px; height: 128px;
    border-radius: 50%;
    background: var(--ink);
  }
  .brand-name {
    font-family: "Oswald", sans-serif;
    font-weight: 700;
    color: var(--orange);
    font-size: 46px;
    line-height: 1.05;
    text-transform: uppercase;
  }
  .brand-name span { display: block; font-size: 24px; }
  .hero-photo {
    position: absolute;
    left: 0; top: 160px;
    width: 849px; height: 560px;
    background: linear-gradient(180deg, var(--sky) 0%, #b9d3e6 28%, #3a6aa6 48%, var(--panel) 75%, #1f3a63 100%);
  }
  .hero-band { position: absolute; left: 0; top: 640px; width: 849px; height: 130px; }
  .question {
    position: absolute;
    left: 40px; right: 40px; top: 560px;
    text-align: center;
    color: var(--orange);
    font-weight: 700;
    font-size: 46px;
    line-height: 1.1;
    text-transform: uppercase;
    text-shadow: 0 2px 6px rgba(0,0,0,.35);
  }
  .reasons-title {
    position: absolute;
    left: 0; right: 0; top: 790px;
    text-align: center;
    color: var(--orange);
    font-weight: 500;
    font-size: 52px;
    text-transform: uppercase;
    letter-spacing: 1px;
  }
  .reasons {
    position: absolute;
    left: 22px; right: 22px; top: 880px;
    height: 210px;
    background: var(--orange);
    display: grid;
    grid-template-columns: repeat(3, 1fr);
    padding: 20px 14px;
  }
  .reason { padding: 0 16px; color: var(--paper); }
  .reason + .reason { border-left: 3px solid var(--paper); }
  .reason-number { font-family: "Oswald", sans-serif; font-weight: 700; font-size: 58px; line-height: 1; }
  .reason-text {
    margin-top: 12px;
    font-family: "Open Sans", sans-serif;
    font-weight: 800;
    font-size: 14px;
    line-height: 1.55;
    text-transform: uppercase;
  }
  .cta {
    position: absolute;
    left: 0; right: 0; top: 1118px;
    text-align: center;
    color: var(--orange);
    font-weight: 700;
    font-size: 44px;
    text-transform: uppercase;
  }
</style>
</head>
<body>
  <main class="flyer">
    <svg class="top-stripe" viewBox="0 0 849 170" aria-hidden="true">
      <polygon points="440,72 849,62 849,96 432,108" fill="var(--orange)"/>
    </svg>

    <div class="hero-photo" role="img" aria-label="Installer kneeling beside solar panels on a residential roof under a blue sky"></div>

    <svg class="hero-band" viewBox="0 0 849 130" aria-hidden="true">
      <polygon points="0,40 849,0 849,50 0,110" fill="var(--orange)"/>
    </svg>

    <header class="brand">
      <div class="brand-dot"></div>
      <div class="brand-name">Tarnbrook<span>Solar &amp; Electrical</span></div>
    </header>

    <h1 class="question">What will your electricity bill<br>look like in 5 years time?</h1>

    <h2 class="reasons-title">3 reasons to install solar.</h2>

    <section class="reasons">
      <div class="reason">
        <div class="reason-number">1.</div>
        <p class="reason-text">The sun provides free, clean energy and is the best way to save money.</p>
      </div>
      <div class="reason">
        <div class="reason-number">2.</div>
        <p class="reason-text">The government provides generous incentives saving you thousands of $$.</p>
      </div>
      <div class="reason">
        <div class="reason-number">3.</div>
        <p class="reason-text">Advancing technology means you can store your energy and use it a night.</p>
      </div>
    </section>

    <p class="cta">Call us now for a free quote</p>
  </main>
</body>
</html>
```